Modern labels for Murlane products

We need a new design of our labels for the product “Murlane” (https://www.murlane-example.eu/#) . The reason why we want to change our labels is to get a modern and more advanced look of our product. We also want to create a unique product that is attractive for our customers, even if the product are used in hospitals and healthcare centers for collecting dangerous waste.

There is three sizes of labels (55x95, 90x95, 170x95 mm) for different boxes, but the label will contain similar information. There are certain requirements and factors from regulations/standards that you need to follow when you create the new layout. But it’s up to you to change the design. You can work with background, fonts, effects, colors, structure, pattern, new symbols, logotype etc. The label could be any color, but the container will stay yellow so they have to look good together.

Keywords: Elegant, modern, functional, attractive, exclusive

Target Market(s)

Hospitals and healthcare centers

Industry/Entity Type

Product

Font styles to use
Serif
Sans Serif

Colors

Designer to choose colors to be used in the design.

Requirements
Must have
• Requirements for the regulations ADR UN3291 and ISO 23907 (PDF).
• * Symbol for danger waste
• * Filling level
• * "Danger"
• * Symbol for no second use
• * Symbol for manufaturer
• * Referencenumber
• * Text "”Clinical waste, Unspecified, N.O.S.”"
• * Area for series, certification, size and useful capacity
• * Area for Illustrations.
• * Text “Autoclavable at 134 c”, “Do not force closure” and “Do not overfill”.
• * Text for certification ”UN 3291 1H2/Y0,3/S/YR/N/QVK7148B”
• Three different sizes (55x95, 90x95, 170x95).
• More info in PDF "3kravspecifikation"
Nice to have
• A modern, elegant, advanced look of our label.
Should not have
• The information must be clear and readable, not too decorative/handwriting fonts.

```html
<!DOCTYPE html>
<html lang="en">
<head>
<meta charset="utf-8">
<title>Murlane clinical waste labels</title>
<link rel="stylesheet" href="https://fonts.googleapis.com/css2?family=Archivo+Black&family=Open+Sans:wght@400;600;700;800&display=swap">
<style>
  :root{
    --yellow:#f8ec17;
    --yellow-bright:#fff200;
    --orange:#f7941d;
    --red:#f15a29;
    --black:#111111;
    --white:#ffffff;
    --navy:#1c2a6b;
  }
  html,body{margin:0;padding:0;overflow:hidden;background:var(--white);}
  .canvas{position:relative;width:1070px;height:1200px;overflow:hidden;background:var(--white);font-family:"Open Sans",Arial,sans-serif;color:var(--black);}
  .sheet{position:absolute;left:5px;top:0;width:1000px;height:1130px;transform:scale(1.06);transform-origin:0 0;}
  .defs{position:absolute;width:0;height:0;overflow:hidden;}

  .label{position:absolute;background:var(--yellow-bright);overflow:hidden;}
  .label--medium{background:var(--yellow);}
  .label *{position:absolute;margin:0;}

  .fill-bar{left:0;top:0;width:100%;background:var(--black);}
  .fill-bar__text{left:0;right:0;text-align:center;color:var(--yellow-bright);font-weight:800;letter-spacing:.04em;white-space:nowrap;}
  .chevrons{display:block;}

  .danger{left:0;right:0;text-align:center;font-family:"Archivo Black",Arial,sans-serif;letter-spacing:.01em;line-height:1;}
  .waste-band{left:0;width:100%;background:var(--orange);}
  .waste-band__text{left:0;right:0;text-align:center;font-weight:700;white-space:nowrap;}
  .stripe{background:var(--orange);}
  .hazard-diamond{display:block;}

  .specs{font-weight:600;white-space:nowrap;}
  .un-code{font-weight:800;line-height:1;white-space:nowrap;}
  .un-code__detail{position:static;display:block;font-weight:700;margin-top:3px;}
  .no-reuse{display:block;}

  .field-label{font-weight:700;white-space:nowrap;}
  .field-icon{display:block;}
  .field-box{background:var(--white);}

  .care-band{left:0;width:100%;background:var(--red);}
  .care-banner{background:var(--orange);clip-path:polygon(2% 0,98% 0,100% 50%,98% 100%,2% 100%,0 50%);display:flex;align-items:center;justify-content:space-around;font-weight:700;white-space:nowrap;}
  .care-banner span{position:static;}
  .care-banner .dot{width:6px;height:6px;border-radius:50%;background:var(--black);}

  .illustration-slot{background:var(--white);}

  .maker{line-height:1.3;white-space:nowrap;}
  .maker__name{position:static;display:flex;align-items:center;gap:4px;font-weight:700;color:var(--navy);line-height:1.1;}
  .maker__name i{position:static;display:inline-block;background:var(--orange);}
  .maker__line{position:static;display:block;}
  .maker__web{font-weight:700;}
  .maker__icon{position:static;display:block;margin-top:4px;}
</style>
</head>
<body>
<div class="canvas">
<svg class="defs" aria-hidden="true">
  <defs>
    <pattern id="chev-left" width="12" height="14" patternUnits="userSpaceOnUse">
      <path d="M6 1 L1 7 L6 13 L10 13 L5 7 L10 1Z" fill="#fff200"/>
    </pattern>
    <pattern id="chev-right" width="12" height="14" patternUnits="userSpaceOnUse">
      <path d="M6 1 L11 7 L6 13 L2 13 L7 7 L2 1Z" fill="#fff200"/>
    </pattern>
    <symbol id="diamond" viewBox="0 0 200 200">
      <polygon points="100,0 200,100 100,200 0,100" fill="#fff"/>
      <polygon points="100,15 185,100 100,185 15,100" fill="#fff" stroke="#111" stroke-width="3.5"/>
      <circle cx="100" cy="72" r="26" fill="#111"/>
      <text x="100" y="162" text-anchor="middle" font-family="Open Sans, sans-serif" font-size="17" fill="#111">6</text>
    </symbol>
    <symbol id="no-reuse" viewBox="0 0 44 44">
      <circle cx="22" cy="22" r="19.5" fill="none" stroke="#111" stroke-width="3"/>
      <text x="22" y="30" text-anchor="middle" font-family="Open Sans, sans-serif" font-weight="800" font-size="22" fill="#111">2</text>
      <line x1="8" y1="36" x2="36" y2="8" stroke="#111" stroke-width="3"/>
    </symbol>
    <symbol id="icon-place" viewBox="0 0 20 20">
      <path d="M10 1 L19 9 L17 9 L17 19 L3 19 L3 9 L1 9Z" fill="#111"/>
      <path d="M8.5 9 h3 v2.5 h2.5 v3 h-2.5 v2.5 h-3 v-2.5 h-2.5 v-3 h2.5z" fill="#fff"/>
    </symbol>
    <symbol id="icon-dept" viewBox="0 0 20 20">
      <rect x="7" y="1" width="6" height="5" fill="#111"/>
      <rect x="1" y="14" width="6" height="5" fill="#111"/>
      <rect x="13" y="14" width="6" height="5" fill="#111"/>
      <path d="M10 6 V10 M4 14 V10 H16 V14" stroke="#111" stroke-width="1.8" fill="none"/>
    </symbol>
    <symbol id="icon-date" viewBox="0 0 20 20">
      <rect x="1.5" y="3" width="17" height="16" fill="none" stroke="#111" stroke-width="2"/>
      <rect x="1.5" y="3" width="17" height="4" fill="#111"/>
      <rect x="5" y="0.5" width="2" height="4" fill="#111"/>
      <rect x="13" y="0.5" width="2" height="4" fill="#111"/>
      <g fill="#111"><rect x="4" y="9" width="3" height="3"/><rect x="8.5" y="9" width="3" height="3"/><rect x="13" y="9" width="3" height="3"/><rect x="4" y="13.5" width="3" height="3"/><rect x="8.5" y="13.5" width="3" height="3"/><rect x="13" y="13.5" width="3" height="3"/></g>
    </symbol>
    <symbol id="icon-factory" viewBox="0 0 20 16">
      <path d="M0 16 V6 L5 9 V6 L10 9 V6 L15 9 V0 H19 V16Z" fill="#111"/>
    </symbol>
  </defs>
</svg>

<div class="sheet">

  <!-- Medium label -->
  <section class="label label--medium" style="left:60px;top:40px;width:494px;height:467px;">
    <div class="fill-bar" style="height:38px;">
      <svg class="chevrons" style="left:8px;top:12px;" width="150" height="14" viewBox="0 0 150 14"><rect width="150" height="14" fill="url(#chev-left)"/></svg>
      <p class="fill-bar__text" style="top:6px;font-size:19px;">FILLING LEVEL</p>
      <svg class="chevrons" style="left:334px;top:12px;" width="150" height="14" viewBox="0 0 150 14"><rect width="150" height="14" fill="url(#chev-left)"/></svg>
    </div>
    <h1 class="danger" style="top:42px;font-size:46px;">DANGER</h1>
    <div class="waste-band" style="top:87px;height:21px;"><p class="waste-band__text" style="top:2px;font-size:12.5px;">CLINICAL WASTE, Unspecified, N.O.S.</p></div>
    <div class="stripe" style="left:345px;top:108px;width:41px;height:262px;"></div>
    <svg class="hazard-diamond" style="left:248px;top:114px;" width="236" height="236" role="img" aria-label="Class 6 infectious substance hazard label"><use href="#diamond"/></svg>
    <p class="specs" style="left:14px;top:124px;font-size:12.5px;line-height:18.5px;">Series: Nova<br>Certification: ISO23907:2012<br>Size: 2,2 L<br>Useful capacity: 1,76 L</p>
    <p class="un-code" style="left:38px;top:220px;font-size:20px;">UN 3291<span class="un-code__detail" style="font-size:8px;margin-left:-4px;">1H2/Y0,3/S/YR/N/QVK7148B</span></p>
    <svg class="no-reuse" style="left:179px;top:212px;" width="42" height="42" role="img" aria-label="Do not reuse"><use href="#no-reuse"/></svg>

    <p class="field-label" style="left:13px;top:282px;font-size:8.5px;">PLACE/CLINIC</p>
    <svg class="field-icon" style="left:86px;top:278px;" width="18" height="18"><use href="#icon-place"/></svg>
    <div class="field-box" style="left:112px;top:278px;width:166px;height:20px;"></div>
    <p class="field-label" style="left:13px;top:311px;font-size:8.5px;">DEPARTMENT</p>
    <svg class="field-icon" style="left:86px;top:307px;" width="18" height="18"><use href="#icon-dept"/></svg>
    <div class="field-box" style="left:112px;top:306px;width:166px;height:20px;"></div>
    <p class="field-label" style="left:13px;top:340px;font-size:8.5px;">SEALING DATE</p>
    <svg class="field-icon" style="left:86px;top:336px;" width="18" height="18"><use href="#icon-date"/></svg>
    <div class="field-box" style="left:112px;top:335px;width:166px;height:21px;"></div>

    <div class="care-band" style="top:373px;height:20px;"></div>
    <div class="care-banner" style="left:14px;top:370px;width:466px;height:26px;font-size:9.5px;padding:0 18px;box-sizing:border-box;"><span>AUTOCLAVABLE AT 134 C</span><span class="dot"></span><span>DO NOT FORCE CLOSURE</span><span class="dot"></span><span>DO NOT OVERFILL</span></div>

    <div class="illustration-slot" style="left:20px;top:404px;width:77px;height:56px;"></div>
    <div class="illustration-slot" style="left:105px;top:404px;width:77px;height:56px;"></div>
    <div class="illustration-slot" style="left:190px;top:404px;width:77px;height:56px;"></div>
    <div class="illustration-slot" style="left:275px;top:404px;width:77px;height:56px;"></div>

    <div class="maker" style="left:366px;top:404px;font-size:8px;">
      <span class="maker__name" style="font-size:15px;"><i style="width:8px;height:8px;"></i>Murlane</span>
      <span class="maker__line">Varnholm, Sweden</span>
      <span class="maker__line maker__web">www.murlane-example.eu</span>
      <span class="maker__line">Ref:&nbsp; xxxxx-xx-xx-xx</span>
      <svg class="maker__icon" style="margin-top:3px;" width="14" height="11"><use href="#icon-factory"/></svg>
    </div>
  </section>

  <!-- Small label -->
  <section class="label label--medium" style="left:628px;top:36px;width:286px;height:492px;">
    <div class="fill-bar" style="height:21px;">
      <svg class="chevrons" style="left:5px;top:6px;" width="86" height="9" viewBox="0 0 134 14"><rect width="134" height="14" fill="url(#chev-left)"/></svg>
      <p class="fill-bar__text" style="top:2px;font-size:12px;">FILLING LEVEL</p>
      <svg class="chevrons" style="left:194px;top:6px;" width="86" height="9" viewBox="0 0 134 14"><rect width="134" height="14" fill="url(#chev-left)"/></svg>
    </div>
    <h1 class="danger" style="top:24px;font-size:47px;">DANGER</h1>
    <div class="waste-band" style="top:76px;height:19px;"><p class="waste-band__text" style="top:2px;font-size:11.5px;">CLINICAL WASTE, Unspecified, N.O.S.</p></div>
    <div class="stripe" style="left:178px;top:95px;width:41px;height:264px;"></div>
    <svg class="hazard-diamond" style="left:125px;top:151px;" width="152" height="152" role="img" aria-label="Class 6 infectious substance hazard label"><use href="#diamond"/></svg>
    <p class="specs" style="left:14px;top:107px;font-size:9.5px;line-height:18.5px;">Series: Nova<br>Certification: ISO23907:2012<br>Size: 2,2 L<br>Useful capacity: 1,76 L</p>
    <p class="un-code" style="left:22px;top:197px;font-size:17px;">UN 3291<span class="un-code__detail" style="font-size:6.5px;margin-left:-12px;margin-top:2px;">1H2/Y0,3/S/YR/N/QVK7148B</span></p>
    <svg class="no-reuse" style="left:15px;top:244px;" width="27" height="27" role="img" aria-label="Do not reuse"><use href="#no-reuse"/></svg>

    <p class="field-label" style="left:6px;top:287px;font-size:5.8px;">PLACE/CLINIC</p>
    <svg class="field-icon" style="left:53px;top:285px;" width="11" height="11"><use href="#icon-place"/></svg>
    <div class="field-box" style="left:70px;top:285px;width:107px;height:13px;"></div>
    <p class="field-label" style="left:6px;top:312px;font-size:5.8px;">DEPARTMENT</p>
    <svg class="field-icon" style="left:53px;top:309px;" width="11" height="11"><use href="#icon-dept"/></svg>
    <div class="field-box" style="left:70px;top:309px;width:107px;height:13px;"></div>
    <p class="field-label" style="left:6px;top:338px;font-size:5.8px;">SEALING DATE</p>
    <svg class="field-icon" style="left:53px;top:335px;" width="11" height="11"><use href="#icon-date"/></svg>
    <div class="field-box" style="left:70px;top:335px;width:107px;height:13px;"></div>

    <div class="care-band" style="top:362px;height:16px;"></div>
    <div class="care-banner" style="left:0;top:360px;width:284px;height:20px;font-size:6.8px;padding:0 8px;box-sizing:border-box;"><span>AUTOCLAVABLE AT 134 C</span><span class="dot" style="width:4px;height:4px;"></span><span>DO NOT FORCE CLOSURE</span><span class="dot" style="width:4px;height:4px;"></span><span>DO NOT OVERFILL</span></div>

    <div class="illustration-slot" style="left:23px;top:390px;width:62px;height:43px;"></div>
    <div class="illustration-slot" style="left:91px;top:390px;width:62px;height:43px;"></div>
    <div class="illustration-slot" style="left:23px;top:441px;width:62px;height:43px;"></div>
    <div class="illustration-slot" style="left:91px;top:441px;width:62px;height:43px;"></div>

    <div class="maker" style="left:178px;top:403px;font-size:6.6px;">
      <span class="maker__name" style="font-size:13px;"><i style="width:7px;height:7px;"></i>Murlane</span>
      <span class="maker__line">Varnholm, Sweden</span>
      <span class="maker__line maker__web">www.murlane-example.eu</span>
      <span class="maker__line">Ref:&nbsp; xxxxx-xx-xx-xx</span>
      <svg class="maker__icon" width="13" height="10"><use href="#icon-factory"/></svg>
    </div>
  </section>

  <!-- Large label -->
  <section class="label" style="left:56px;top:576px;width:883px;height:492px;">
    <div class="fill-bar" style="height:38px;">
      <svg class="chevrons" style="left:20px;top:10px;" width="290" height="18" viewBox="0 0 174 14" preserveAspectRatio="none"><rect width="174" height="14" fill="url(#chev-left)"/></svg>
      <p class="fill-bar__text" style="top:4px;font-size:23px;">FILLING LEVEL</p>
      <svg class="chevrons" style="left:570px;top:10px;" width="290" height="18" viewBox="0 0 174 14" preserveAspectRatio="none"><rect width="174" height="14" fill="url(#chev-right)"/></svg>
    </div>
    <h1 class="danger" style="top:43px;font-size:64px;">DANGER</h1>
    <div class="waste-band" style="top:101px;height:22px;"><p class="waste-band__text" style="top:2px;font-size:13.5px;">CLINICAL WASTE, Unspecified, N.O.S.</p></div>
    <div class="stripe" style="left:665px;top:123px;width:55px;height:256px;"></div>
    <svg class="hazard-diamond" style="left:576px;top:132px;" width="216" height="216" role="img" aria-label="Class 6 infectious substance hazard label"><use href="#diamond"/></svg>
    <p class="specs" style="left:73px;top:134px;font-size:13px;line-height:18.5px;">Series: Nova<br>Certification: ISO23907:2012<br>Size: 2,2 L<br>Useful capacity: 1,76 L</p>
    <p class="un-code" style="left:341px;top:147px;font-size:20px;">UN 3291<span class="un-code__detail" style="font-size:8px;margin-left:-18px;">1H2/Y0,3/S/YR/N/QVK7148B</span></p>
    <svg class="no-reuse" style="left:495px;top:143px;" width="44" height="44" role="img" aria-label="Do not reuse"><use href="#no-reuse"/></svg>

    <p class="field-label" style="left:72px;top:235px;font-size:12.5px;">PLACE/CLINIC</p>
    <svg class="field-icon" style="left:174px;top:231px;" width="24" height="24"><use href="#icon-place"/></svg>
    <div class="field-box" style="left:209px;top:230px;width:232px;height:28px;"></div>
    <p class="field-label" style="left:72px;top:277px;font-size:12.5px;">DEPARTMENT</p>
    <svg class="field-icon" style="left:174px;top:273px;" width="24" height="24"><use href="#icon-dept"/></svg>
    <div class="field-box" style="left:209px;top:270px;width:232px;height:28px;"></div>
    <p class="field-label" style="left:69px;top:318px;font-size:12.5px;">SEALING DATE</p>
    <svg class="field-icon" style="left:174px;top:313px;" width="24" height="24"><use href="#icon-date"/></svg>
    <div class="field-box" style="left:209px;top:311px;width:232px;height:28px;"></div>

    <div class="care-band" style="top:356px;height:23px;"></div>
    <div class="care-banner" style="left:41px;top:352px;width:575px;height:32px;font-size:11px;padding:0 20px;box-sizing:border-box;"><span>AUTOCLAVABLE AT 134 C</span><span class="dot"></span><span>DO NOT FORCE CLOSURE</span><span class="dot"></span><span>DO NOT OVERFILL</span></div>

    <div class="illustration-slot" style="left:59px;top:400px;width:125px;height:81px;"></div>
    <div class="illustration-slot" style="left:197px;top:400px;width:123px;height:81px;"></div>
    <div class="illustration-slot" style="left:333px;top:400px;width:124px;height:81px;"></div>
    <div class="illustration-slot" style="left:471px;top:400px;width:125px;height:81px;"></div>

    <div class="maker" style="left:673px;top:388px;font-size:11px;">
      <span class="maker__name" style="font-size:21px;"><i style="width:10px;height:10px;"></i>Murlane</span>
      <span class="maker__line">Varnholm, Sweden</span>
      <span class="maker__line maker__web">www.murlane-example.eu</span>
      <span class="maker__line">Ref:&nbsp; xxxxx-xx-xx-xx</span>
      <svg class="maker__icon" style="margin-top:10px;" width="21" height="17"><use href="#icon-factory"/></svg>
    </div>
  </section>

</div>
</div>
</body>
</html>
```